Heronbrook Custom Woodcraft Website design

Need a small website to showcase my products and take orders

would also like payment options

We do custom wood work along with cnc work in wood plastic and soft metals

we are based in edmonton alberta canada
Updates

Industry/Entity Type

Work

Number of Pages Required

3 page

Requirements
Nice to have
• Interview for for a woodworking magazine
• http://grainandplaneweekly.example/issue-1-02-august-2016/member-spotlight
• I would also like to see metal working/branding iron info
• Also adding the picture of me from the above interview is a nice touch

```html
<!DOCTYPE html>
<html lang="en">
<head>
<meta charset="utf-8">
<title>Heronbrook Custom Woodcraft</title>
<link href="https://fonts.googleapis.com/css2?family=Cinzel:wght@400;700&family=Open+Sans:wght@300;400;600&display=swap" rel="stylesheet">
<style>
:root{
  --brown:#7b3e05;
  --brown-dark:#5a2c04;
  --brown-deep:#3a1c03;
  --accent:#8a4306;
  --cream:#f4dcae;
  --text:#333;
  --muted:#777;
  --line:#c9c9c9;
  --white:#fff;
}
*{margin:0;padding:0;box-sizing:border-box}
html,body{width:766px;height:1200px;overflow:hidden}
body{position:relative;font-family:'Open Sans',sans-serif;color:var(--text);background:var(--white)}
.abs{position:absolute}
.topbar{left:0;top:0;width:766px;height:69px;background:var(--brown)}
.account-links{left:110px;top:12px;font-size:8.5px;color:var(--white);display:flex;gap:6px}
.logo{left:0;width:766px;top:12px;text-align:center;font-family:'Cinzel',serif;font-weight:700;color:var(--white);line-height:1}
.logo .l1{font-size:20px;letter-spacing:1px}
.logo .l2{font-size:10.5px;letter-spacing:1.2px;margin-top:2px}
.cart{left:632px;top:5px;width:25px;height:25px;background:var(--white);border-radius:2px}
.hero{left:0;top:69px;width:766px;height:323px;background:linear-gradient(100deg,#7a4526 0%,#5b3420 26%,#2a2523 30%,#6a6a68 45%,#4a4a48 62%,#2b2b2b 68%,#3e3e3e 100%)}
.nav{left:0;top:69px;width:766px;height:32px;background:rgba(20,15,12,.72);font-size:9.5px;color:var(--white)}
.nav a{position:absolute;top:9px;color:var(--white);text-decoration:none}
.nav a.active{color:var(--cream)}
.search{left:641px;top:8px;width:16px;height:16px;border:1px solid var(--white)}
.hero-title{left:0;width:766px;top:176px;text-align:center;font-family:'Cinzel',serif;font-weight:700;font-size:28px;color:var(--cream);letter-spacing:1px}
.hero-sub{left:0;width:766px;top:216px;text-align:center;font-size:12.5px;color:var(--white)}
.shop{left:322px;top:266px;width:122px;height:31px;border:2px solid var(--white);border-radius:16px;color:var(--white);font-size:13px;text-align:center;line-height:27px}
.arrow{top:216px;width:32px;height:32px;border:1.5px solid var(--white);border-radius:50%}
.section-title{left:0;width:766px;top:446px;text-align:center;font-size:22px;font-weight:400;color:var(--brown-dark);letter-spacing:.5px}
.section-sub{left:0;width:766px;top:485px;text-align:center;font-size:10px;color:var(--muted);line-height:14px}
.card{top:554px;width:131px;height:98px;border:1px solid #c4c4c4;border-radius:3px;background:#f3f3f3}
.card .tag{position:absolute;left:14px;top:8px;font-size:9px;color:var(--accent)}
.card .photo{position:absolute;left:13px;top:28px;width:105px;height:57px}
.pname{top:673px;width:131px;text-align:center;font-size:9px;line-height:11.5px;color:var(--text)}
.price{top:705px;width:131px;text-align:center;font-size:9.5px}
.price b{color:var(--accent);font-weight:600}
.price s{color:#444}
.btn-cart{top:742px;width:60px;height:18px;background:var(--accent);color:var(--white);border-radius:9px;font-size:7px;text-align:center;line-height:18px}
.icon-btn{top:744px;width:15px;height:15px;border:1px solid #aaa;border-radius:50%}
.icon-btn svg{display:block}
.load{left:329px;top:806px;width:109px;height:30px;border:1px solid #999;border-radius:15px;font-size:10px;text-align:center;line-height:28px;color:#555}
.rule{left:0;top:868px;width:766px;height:1px;background:var(--line)}
.nl-title{left:110px;top:882px;font-size:15px;color:var(--brown-deep)}
.nl-sub{left:110px;top:905px;font-size:10px;color:var(--muted)}
.email{left:110px;top:929px;width:234px;height:27px;border:1px solid #bbb;border-radius:14px;font-size:8.5px;color:#999;padding:7px 6px}
.subscribe{left:353px;top:930px;width:83px;height:26px;background:var(--brown-deep);border-radius:13px;color:var(--white);font-size:10px;text-align:center;line-height:26px}
.follow{left:560px;top:882px;font-size:15px;color:var(--brown-deep)}
.social{top:914px;width:15px;height:15px;border-radius:50%;background:var(--brown-deep)}
.footer{left:0;top:979px;width:766px;height:181px;background:var(--brown-dark)}
.fcol{top:1001px;color:var(--white)}
.fcol h3{font-weight:400;font-size:11.5px;margin-bottom:16px}
.fcol li{list-style:none;font-size:8px;line-height:16px;color:#f0e6dc}
.copy{left:0;top:1160px;width:766px;height:40px;background:var(--brown-deep);text-align:center;font-size:7.5px;color:#8d6a4c;line-height:40px}
</style>
</head>
<body>
<div class="abs topbar"></div>
<div class="abs account-links"><span>My account</span><span>|</span><span>Wishlist</span><span>|</span><span>log in</span></div>
<div class="abs logo"><div class="l1">HERONBROOK</div><div class="l2">CUSTOM WOODCRAFT</div></div>
<div class="abs cart"><svg width="25" height="25" viewBox="0 0 25 25"><path d="M6 8h2l2 7h7l2-5H9" fill="none" stroke="#5a2c04" stroke-width="1.2"/><circle cx="11" cy="18" r="1" fill="#5a2c04"/><circle cx="16" cy="18" r="1" fill="#5a2c04"/></svg></div>

<div class="abs hero" role="img" aria-label="Carved wooden panels and a CNC-engraved plaque"></div>
<nav class="abs nav">
  <a class="active" style="left:110px">Home</a>
  <a style="left:178px">Products</a>
  <a style="left:260px">Blog</a>
  <a style="left:322px">Sale</a>
  <a style="left:382px">About us</a>
  <a style="left:464px">Contact us</a>
  <span class="abs search"><svg width="14" height="14" viewBox="0 0 14 14"><circle cx="8" cy="6" r="2.6" fill="none" stroke="#fff"/><path d="M6 8l-2.5 2.5" stroke="#fff"/></svg></span>
</nav>
<div class="abs hero-title">CURABITUR IACULIS MAURIS FELIS</div>
<div class="abs hero-sub">Pulvinar interdum justo elementum eget Integer nulla purus rhoncus non luctus</div>
<div class="abs shop">SHOP NOW</div>
<div class="abs arrow" style="left:56px"><svg width="29" height="29" viewBox="0 0 29 29"><path d="M17 8l-6 6.5 6 6.5" fill="none" stroke="#fff" stroke-width="2"/></svg></div>
<div class="abs arrow" style="left:678px"><svg width="29" height="29" viewBox="0 0 29 29"><path d="M12 8l6 6.5-6 6.5" fill="none" stroke="#fff" stroke-width="2"/></svg></div>

<h2 class="abs section-title">Featured Products</h2>
<p class="abs section-sub">Sed suscipit ligula sed scelerisque consectetur Donec a sem ultrices risus convallis<br>commodo Quisque ornare in lorem ac lobortis</p>

<div class="abs card" style="left:109px"><span class="tag">Aenean pulvinar</span><div class="photo" role="img" aria-label="Set of wooden side tables" style="background:linear-gradient(#8a6a4a,#c79a62 60%,#ddd)"></div></div>
<div class="abs card" style="left:248px"><span class="tag">Aenean pulvinar</span><div class="photo" role="img" aria-label="Carved oval cribbage board" style="background:radial-gradient(ellipse at center,#d9b98a 45%,#2c2620 62%)"></div></div>
<div class="abs card" style="left:387px"><span class="tag">Aenean pulvinar</span><div class="photo" role="img" aria-label="Engraved round plaque on dark stand" style="background:radial-gradient(circle at center,#1c1c1c 35%,#4a5a6e 70%,#dcdcdc)"></div></div>
<div class="abs card" style="left:526px"><span class="tag">Aenean pulvinar</span><div class="photo" role="img" aria-label="Pine display stands" style="background:linear-gradient(#6e4a30,#c58c5a 60%,#e2c8a8)"></div></div>

<div class="abs pname" style="left:109px">Morbi mattis porttitor ipsum<br>et feugiat</div>
<div class="abs pname" style="left:248px">Morbi mattis porttitor ipsum<br>et feugiat</div>
<div class="abs pname" style="left:387px">Morbi mattis porttitor ipsum<br>et feugiat</div>
<div class="abs pname" style="left:526px">Morbi mattis porttitor ipsum<br>et feugiat</div>
<div class="abs price" style="left:109px"><b>From$100.00</b> <s>$125.00</s></div>
<div class="abs price" style="left:248px"><b>From$100.00</b> <s>$125.00</s></div>
<div class="abs price" style="left:387px"><b>From$100.00</b> <s>$125.00</s></div>
<div class="abs price" style="left:526px"><b>From$100.00</b> <s>$125.00</s></div>

<div class="abs btn-cart" style="left:110px">ADD TO CART</div>
<div class="abs icon-btn" style="left:202px"><svg width="13" height="13" viewBox="0 0 13 13"><path d="M6.5 10L3 6.5a1.8 1.8 0 0 1 3.5-2.2 1.8 1.8 0 0 1 3.5 2.2z" fill="none" stroke="#555" stroke-width=".8"/></svg></div>
<div class="abs icon-btn" style="left:224px"><svg width="13" height="13" viewBox="0 0 13 13"><circle cx="7.5" cy="5.5" r="2" fill="none" stroke="#555" stroke-width=".8"/><path d="M6 7L4 9" stroke="#555" stroke-width=".9"/></svg></div>
<div class="abs btn-cart" style="left:249px">ADD TO CART</div>
<div class="abs icon-btn" style="left:341px"><svg width="13" height="13" viewBox="0 0 13 13"><path d="M6.5 10L3 6.5a1.8 1.8 0 0 1 3.5-2.2 1.8 1.8 0 0 1 3.5 2.2z" fill="none" stroke="#555" stroke-width=".8"/></svg></div>
<div class="abs icon-btn" style="left:363px"><svg width="13" height="13" viewBox="0 0 13 13"><circle cx="7.5" cy="5.5" r="2" fill="none" stroke="#555" stroke-width=".8"/><path d="M6 7L4 9" stroke="#555" stroke-width=".9"/></svg></div>
<div class="abs btn-cart" style="left:388px">ADD TO CART</div>
<div class="abs icon-btn" style="left:479px"><svg width="13" height="13" viewBox="0 0 13 13"><path d="M6.5 10L3 6.5a1.8 1.8 0 0 1 3.5-2.2 1.8 1.8 0 0 1 3.5 2.2z" fill="none" stroke="#555" stroke-width=".8"/></svg></div>
<div class="abs icon-btn" style="left:501px"><svg width="13" height="13" viewBox="0 0 13 13"><circle cx="7.5" cy="5.5" r="2" fill="none" stroke="#555" stroke-width=".8"/><path d="M6 7L4 9" stroke="#555" stroke-width=".9"/></svg></div>
<div class="abs btn-cart" style="left:527px">ADD TO CART</div>
<div class="abs icon-btn" style="left:618px"><svg width="13" height="13" viewBox="0 0 13 13"><path d="M6.5 10L3 6.5a1.8 1.8 0 0 1 3.5-2.2 1.8 1.8 0 0 1 3.5 2.2z" fill="none" stroke="#555" stroke-width=".8"/></svg></div>
<div class="abs icon-btn" style="left:640px"><svg width="13" height="13" viewBox="0 0 13 13"><circle cx="7.5" cy="5.5" r="2" fill="none" stroke="#555" stroke-width=".8"/><path d="M6 7L4 9" stroke="#555" stroke-width=".9"/></svg></div>

<div class="abs load">LOAD MORE</div>
<div class="abs rule"></div>

<div class="abs nl-title">Newsletter</div>
<div class="abs nl-sub">Enter your email address to join our mailing list</div>
<div class="abs email">Enter your email</div>
<div class="abs subscribe">SUBSCRIBE</div>
<div class="abs follow">Follow us</div>
<div class="abs social" style="left:562px"></div>
<div class="abs social" style="left:589px"></div>
<div class="abs social" style="left:615px"></div>
<div class="abs social" style="left:641px"></div>

<footer class="abs footer"></footer>
<div class="abs fcol" style="left:110px"><h3>Information</h3><ul><li>Home</li><li>Collection</li><li>Search</li><li>Blog</li><li>About us</li><li>Contact us</li><li>Sitemap</li></ul></div>
<div class="abs fcol" style="left:248px"><h3>Why buy from us</h3><ul><li>Shipping &amp; Returns</li><li>Secure Shopping</li><li>International Shipping</li><li>Affiliates</li><li>Group Sales</li></ul></div>
<div class="abs fcol" style="left:387px"><h3>My account</h3><ul><li>My Account</li><li>My Addresses</li><li>My Cart</li></ul></div>
<div class="abs fcol" style="left:526px"><h3>Contacts</h3><ul><li style="line-height:11px">Heronbrook Workshop<br>T5J 0A1</li><li style="margin-top:4px">&#9990;&nbsp; 1-555-0100-246</li><li>&#9993;&nbsp; info@heronbrook.example</li></ul></div>
<div class="abs copy">© 2016Heronbrookcustomwoodcraft.all right reserved</div>
</body>
</html>
```